Einladungskarten-Design zur Einweihung von neuen Räumlichkeiten eines Planungsdienstleisters für Elektro- sowie IT-Lösungen
Zielgruppe
Planungsleistung für Elektro sowie IT Lösungen
Aufgabenstellung
Einladung zur Einweihung der neuen Räumlichkeiten, am 09. November 2024, beginn 16:00 Uhr. Einladung durch Geschäftsführer E-Strommark GmbH - Tobias Kernbichl und Geschäftsführer IT-Strommark GmbH - Florian Wetzbacher
Ort:
E-Strommark GmbH, IT-Strommark GmbH
Lerchenfeldstr. 14
88472 Lindenhausen
Anmeldung, Rückmeldung per Mail an
info@e-strommark.de

```html
<!DOCTYPE html>
<html lang="de">
<head>
<meta charset="utf-8">
<title>Einladung – Einweihung neuer Räumlichkeiten</title>
<link rel="stylesheet" href="https://fonts.googleapis.com/css2?family=Bebas+Neue&family=Oswald:wght@300;500&display=swap">
<style>
  :root {
    --page-bg: #ffffff;
    --card-bg: #ffffff;
    --navy: #3b3b5e;
    --navy-light: #4a4a75;
    --stripe-blue: #4f9fd6;
    --stripe-green: #9cc41c;
    --ink: #111111;
    --logo-ink: #555555;
  }
  * { margin: 0; padding: 0; box-sizing: border-box; }
  html, body {
    width: 929px; height: 1200px; overflow: hidden;
    background: var(--page-bg);
  }
  .sheet {
    position: relative; width: 929px; height: 1200px;
    display: flex; justify-content: center; align-items: center; gap: 50px;
  }
  .card {
    position: relative; width: 400px; height: 568px;
    background: var(--card-bg);
    box-shadow: 6px 8px 10px rgba(0,0,0,0.35);
    overflow: hidden;
    text-align: center;
    font-family: "Oswald", "Arial Narrow", sans-serif;
    font-weight: 300;
    text-transform: uppercase;
    color: var(--ink);
  }
  .edge-pattern {
    position: absolute; top: 0; bottom: 0; width: 45px;
    background: linear-gradient(180deg, var(--navy) 0%, var(--navy-light) 45%, var(--navy) 100%);
  }
  .edge-pattern.left { left: 0; }
  .edge-pattern.right { right: 0; width: 57px; }
  .stripe { position: absolute; top: 0; bottom: 0; }
  .stripe.blue-left { left: 45px; width: 6px; background: var(--stripe-blue); }
  .stripe.green-left { left: 51px; width: 7px; background: var(--stripe-green); }
  .stripe.green-right { right: 63px; width: 6px; background: var(--stripe-green); }
  .stripe.blue-right { right: 57px; width: 6px; background: var(--stripe-blue); }

  .content { position: absolute; left: 58px; right: 69px; top: 0; bottom: 0; }
  .block { position: absolute; left: 0; right: 0; }

  .title {
    top: 70px;
    font-family: "Bebas Neue", "Oswald", sans-serif;
    font-size: 54px; line-height: 1; letter-spacing: 0.5px;
    font-weight: 400;
  }
  .subtitle { top: 118px; font-size: 12.5px; line-height: 1; }

  .info { font-size: 13.5px; line-height: 19.5px; }
  .info .label { font-weight: 500; }
  .where { top: 180px; }
  .when { top: 273px; }
  .rsvp { top: 366px; }

  .brand {
    display: flex; justify-content: center; align-items: center; gap: 6px;
    font-size: 22px; line-height: 1; letter-spacing: 0.5px;
    color: var(--logo-ink);
  }
  .brand .dot { width: 9px; height: 9px; border-radius: 50%; }
  .brand.electric .dot { background: var(--stripe-blue); }
  .brand.it .dot { background: var(--stripe-green); }
  .front .brand.electric { top: 440px; }
  .front .brand.it { top: 485px; }
  .back .brand.electric { top: 204px; }
  .back .brand.it { top: 306px; }

  .hosts { top: 530px; font-size: 7px; line-height: 11px; font-weight: 500; letter-spacing: -0.1px; }
</style>
</head>
<body>
<main class="sheet">

  <section class="card front" aria-label="Einladungskarte Vorderseite">
    <div class="edge-pattern left" role="img" aria-label="Dekoratives Netzwerkmuster aus Kreisen und Leiterbahnen in Dunkelblau und Cyan"></div>
    <div class="stripe blue-left"></div>
    <div class="stripe green-left"></div>
    <div class="stripe green-right"></div>
    <div class="stripe blue-right"></div>
    <div class="edge-pattern right" role="img" aria-label="Dekoratives Netzwerkmuster aus Kreisen und Leiterbahnen in Dunkelblau und Cyan"></div>

    <div class="content">
      <h1 class="block title">Enladung</h1>
      <p class="block subtitle">Einweihung neuer Räumlichkeiten</p>

      <div class="block info where">
        <p class="label">Wo?</p>
        <p>E-Strommark GmbH, IT-Strommark GmbH</p>
        <p>Lerchenfeldstr. 14</p>
        <p>88472 Lindenhausen</p>
      </div>

      <div class="block info when">
        <p class="label">Wann?</p>
        <p>09. November 2024</p>
        <p>Beginn: 16 Uhr</p>
      </div>

      <div class="block info rsvp">
        <p class="label">Anmeldung, Rückmeldung per Mail an</p>
        <p>info@e-strommark.de</p>
      </div>

      <p class="block brand electric"><span class="dot"></span>E-Strommark</p>
      <p class="block brand it"><span class="dot"></span>IT-Strommark</p>

      <p class="block hosts">Einladung durch Geschäftsführer E-Strommark GmbH - Tobias Kernbichl<br>und Geschäftsführer IT-Strommark GmbH - Florian Wetzbacher</p>
    </div>
  </section>

  <section class="card back" aria-label="Einladungskarte Rückseite">
    <div class="edge-pattern left" role="img" aria-label="Dekoratives Netzwerkmuster aus Kreisen und Leiterbahnen in Dunkelblau und Cyan"></div>
    <div class="stripe blue-left"></div>
    <div class="stripe green-left"></div>
    <div class="stripe green-right"></div>
    <div class="stripe blue-right"></div>
    <div class="edge-pattern right" role="img" aria-label="Dekoratives Netzwerkmuster aus Kreisen und Leiterbahnen in Dunkelblau und Cyan"></div>

    <div class="content">
      <p class="block brand electric"><span class="dot"></span>E-Strommark</p>
      <p class="block brand it"><span class="dot"></span>IT-Strommark</p>
    </div>
  </section>

</main>
</body>
</html>
```